New Business Card Design Project

New business card design required for an electrical business in Australia. Offering quality electrical services including design and installation. Electrical services offered are domestic, commercial and industrial. Also meets all the air conditioning installation and maintenance needs.

Target Market(s)

The business is sleek, professional and caters primarily to wealthy clients and government contracts looking for exceptional, tailored service.

Industry/Entity Type

Electrical

Contact Information for Business Card

Damian Corlowe (Director)
0438 615 274
admin@vrtelectrical.com.au
www.vrtelectrical.com.au

Font styles to use
Sans Serif

Requirements
Must have
• The business card must show the license number - 64193 to comply with legislation.
Nice to have
• The logo colours and fonts could be incorporated into the design if the designer sees fit. We are open to new ideas and welcome creativity. The logo style guide is attached for reference if required.

```html
<!DOCTYPE html>
<html lang="en">
<head>
<meta charset="utf-8">
<title>VRT Electrical – Business Card</title>
<link href="https://fonts.googleapis.com/css2?family=Arimo:wght@400;700&display=swap" rel="stylesheet">
<style>
  :root {
    --navy: #0f2a57;
    --navy-light: #1d3b6e;
    --ink: #3a3a3a;
    --rule: #555b63;
    --paper: #ffffff;
    --backdrop: #e6e7ea;
  }
  * { box-sizing: border-box; margin: 0; padding: 0; }
  html, body { width: 1200px; height: 900px; overflow: hidden; }
  body {
    background: var(--backdrop);
    font-family: "Arimo", Arial, sans-serif;
    display: flex;
    flex-direction: column;
    align-items: center;
    justify-content: center;
    gap: 40px;
  }
  .card {
    width: 660px;
    height: 400px;
    border-radius: 28px;
    position: relative;
    overflow: hidden;
    box-shadow: 0 6px 18px rgba(0,0,0,0.18);
  }
  .card-front {
    background: linear-gradient(135deg, var(--navy) 0%, var(--navy) 55%, var(--navy-light) 100%);
    display: flex;
    align-items: center;
    justify-content: center;
  }
  .wordmark {
    display: flex;
    align-items: center;
    gap: 14px;
    font-weight: 700;
    letter-spacing: 0.04em;
    line-height: 1;
  }
  .wordmark-name { font-size: 44px; }
  .wordmark-dot {
    width: 14px; height: 14px; border-radius: 50%;
  }
  .card-front .wordmark { color: var(--paper); }
  .card-front .wordmark-dot { background: var(--paper); }

  .card-back { background: var(--paper); }
  .card-back .wordmark {
    position: absolute;
    top: 58px;
    right: 60px;
    color: var(--navy);
  }
  .card-back .wordmark-name { font-size: 38px; }
  .card-back .wordmark-dot { background: var(--navy); }

  .divider {
    position: absolute;
    left: 60px;
    right: 60px;
    top: 196px;
    height: 1.5px;
    background: var(--rule);
  }
  .holder-name {
    position: absolute;
    left: 60px;
    top: 164px;
    font-size: 26px;
    font-weight: 700;
    color: var(--navy);
    letter-spacing: 0.01em;
  }
  .license {
    position: absolute;
    right: 60px;
    top: 170px;
    font-size: 18px;
    color: var(--ink);
  }
  .holder-role {
    position: absolute;
    left: 60px;
    top: 208px;
    font-size: 19px;
    color: var(--ink);
  }
  .contacts {
    position: absolute;
    left: 60px;
    top: 250px;
    list-style: none;
    display: flex;
    flex-direction: column;
    gap: 10px;
  }
  .contact {
    display: flex;
    align-items: center;
    gap: 14px;
    font-size: 19px;
    color: var(--ink);
  }
  .contact svg { width: 20px; height: 20px; flex: none; }
  .contact svg .ico { fill: var(--navy); }
</style>
</head>
<body>

  <section class="card card-front" aria-label="Card front">
    <div class="wordmark">
      <span class="wordmark-name">VRT ELECTRICAL</span>
      <span class="wordmark-dot"></span>
    </div>
  </section>

  <section class="card card-back" aria-label="Card back">
    <div class="wordmark">
      <span class="wordmark-name">VRT ELECTRICAL</span>
      <span class="wordmark-dot"></span>
    </div>

    <h1 class="holder-name">DAMIAN CORLOWE</h1>
    <p class="license">license number - 64193</p>
    <div class="divider"></div>
    <p class="holder-role">Director</p>

    <ul class="contacts">
      <li class="contact">
        <svg viewBox="0 0 24 24" aria-hidden="true">
          <path class="ico" d="M6.6 10.8a15.1 15.1 0 0 0 6.6 6.6l2.2-2.2a1 1 0 0 1 1-.25 11.4 11.4 0 0 0 3.6.57 1 1 0 0 1 1 1V20a1 1 0 0 1-1 1A17 17 0 0 1 3 4a1 1 0 0 1 1-1h3.5a1 1 0 0 1 1 1c0 1.25.2 2.45.57 3.6a1 1 0 0 1-.25 1z"/>
        </svg>
        <span>0438 615 274</span>
      </li>
      <li class="contact">
        <svg viewBox="0 0 24 24" aria-hidden="true">
          <path class="ico" d="M2 5h20v14H2z M3.5 6.5 12 12.5l8.5-6z" fill-rule="evenodd"/>
        </svg>
        <span>admin@vrtelectrical.com.au</span>
      </li>
      <li class="contact">
        <svg viewBox="0 0 24 24" aria-hidden="true">
          <path class="ico" fill-rule="evenodd" d="M12 2a10 10 0 1 1 0 20 10 10 0 0 1 0-20zm0 2a8 8 0 0 0-7.9 7h3.9c.1-2.6.7-5 1.7-6.6A8 8 0 0 0 12 4zm0 0c-1.2 1.4-1.9 4-2 7h4c-.1-3-.8-5.6-2-7zm2.3.4c1 1.6 1.6 4 1.7 6.6h3.9a8 8 0 0 0-5.6-6.6zM4.1 13a8 8 0 0 0 5.6 6.6c-1-1.6-1.6-4-1.7-6.6zm5.9 0c.1 3 .8 5.6 2 7 1.2-1.4 1.9-4 2-7zm6 0c-.1 2.6-.7 5-1.7 6.6a8 8 0 0 0 5.6-6.6z"/>
        </svg>
        <span>www.vrtelectrical.com.au</span>
      </li>
    </ul>
  </section>

</body>
</html>
```